Corporate Profile, with ALOT more work for winning bidder

We need
1. CD designed
2. CD Cover Designed
3. 2x Envelope's designed
4. Letter head designed
The designer picked will also get many further projects from us. Almost totaling 10k a year.
- More info
• Software installation disc
a. Logo
b. Contact details (See below)
c. Instructions
o “Please insert CD into computer and follow the prompts”
d. Title
o “Free Software Installation Disc”
• CD Sleave double sided
- Front
o Logo
o Website Address
o Facebook address
o Title
? “Free Software Installation Disc”
• Letter head
- Logo
- Contact information
- A4 paper size
• C4 Envelope
- Nicely Designed with logo
- A window to put address
- Printed return address (See below) on back
• DL Envelope, to return to us
- Had our return address ( See below)
- Nice design
Contact details
Pixel Harbour Co
17b Tamsin Crescent Larkfield, Vic, 3198
www.PixelHarbourCo.com.au
1300 42 19 58
www.Chatterloop.com/PixelHarbourCo
Return Address
Pixel Harbour Co
17b Tamsin Crescent
Larkfield, Vic, 3198

```html
<!DOCTYPE html>
<html lang="en">
<head>
<meta charset="utf-8">
<title>Pixel Harbour Co – DL Envelopes</title>
<link rel="stylesheet" href="https://fonts.googleapis.com/css2?family=Arimo:wght@400;700&family=Source+Sans+3:wght@400&display=swap">
<style>
  :root {
    --page-bg: #ffffff;
    --envelope-light: #6f6f72;
    --envelope-dark: #58585a;
    --brand-blue: #1aa3d9;
    --brand-orange: #f7941d;
    --text-light: #ffffff;
    --caption-grey: #b8b8b8;
    --window-fill: #e1e2e4;
    --window-edge: #2e2e30;
  }
  html, body {
    margin: 0;
    padding: 0;
    width: 1200px;
    height: 849px;
    overflow: hidden;
    background: var(--page-bg);
  }
  .sheet {
    position: relative;
    width: 1200px;
    height: 849px;
    font-family: "Arimo", Arial, sans-serif;
  }
  .envelope {
    position: absolute;
    width: 630px;
    height: 315px;
    background: var(--envelope-light);
    overflow: hidden;
  }
  .envelope--return { left: 96px; top: 75px; }
  .envelope--window { left: 464px; top: 452px; }
  .envelope__curve {
    position: absolute;
    left: 0;
    top: 0;
    width: 630px;
    height: 315px;
  }
  .return-address {
    position: absolute;
    color: var(--text-light);
  }
  .envelope--return .return-address {
    left: 78px;
    top: 99px;
    font-size: 17px;
    line-height: 1.27;
  }
  .envelope--window .return-address {
    left: 91px;
    top: 27px;
    font-size: 14px;
    font-weight: 700;
    line-height: 1.34;
  }
  .return-address__note {
    font-size: 10px;
    font-weight: 400;
    letter-spacing: 1.6px;
    margin-bottom: 2px;
  }
  .return-address__name {
    letter-spacing: 2px;
    font-weight: 700;
    text-transform: uppercase;
  }
  .envelope--return .return-address__name { font-size: 16px; }
  .envelope--window .return-address__name { font-size: 14px; }
  .return-address__name .accent { color: var(--brand-orange); }
  .return-address__name .primary { color: var(--brand-blue); }
  .brand-mark {
    position: absolute;
    display: flex;
    flex-direction: column;
    align-items: center;
    gap: 20px;
    width: 200px;
  }
  .envelope--return .brand-mark { left: 400px; top: 168px; }
  .envelope--window .brand-mark { left: 401px; top: 168px; }
  .brand-mark__dot {
    width: 62px;
    height: 62px;
    border-radius: 50%;
    background: var(--brand-blue);
  }
  .brand-mark__name {
    color: var(--brand-blue);
    font-weight: 700;
    font-size: 20px;
    white-space: nowrap;
  }
  .address-window {
    position: absolute;
    left: 92px;
    top: 189px;
    width: 270px;
    height: 78px;
    border-radius: 10px;
    background: var(--window-fill);
    border: 1.5px solid var(--window-edge);
  }
  .caption {
    position: absolute;
    font-family: "Source Sans 3", "PT Sans", Arial, sans-serif;
    font-size: 20px;
    color: var(--caption-grey);
  }
  .caption--return { left: 96px; top: 403px; }
  .caption--window { left: 464px; top: 777px; }
</style>
</head>
<body>
<main class="sheet">

  <section class="envelope envelope--return">
    <svg class="envelope__curve" viewBox="0 0 630 315" aria-hidden="true">
      <defs>
        <filter id="curve-shadow-a" x="-10%" y="-10%" width="130%" height="130%">
          <feDropShadow dx="4" dy="3" stdDeviation="4" flood-color="#000" flood-opacity="0.45"/>
        </filter>
      </defs>
      <path d="M0,0 H356 C378,150 260,290 0,313 V0 Z" fill="var(--envelope-dark)" filter="url(#curve-shadow-a)"/>
    </svg>
    <div class="return-address">
      <div class="return-address__name"><span class="primary">Pixel Harbour</span> <span class="accent">Co</span></div>
      <div>17b Tamsin Crescent</div>
      <div>Larkfield, Vic, 3198</div>
    </div>
    <div class="brand-mark">
      <div class="brand-mark__dot"></div>
      <div class="brand-mark__name">PIXEL HARBOUR CO</div>
    </div>
  </section>
  <div class="caption caption--return">DL Return Envelope</div>

  <section class="envelope envelope--window">
    <svg class="envelope__curve" viewBox="0 0 630 315" aria-hidden="true">
      <defs>
        <filter id="curve-shadow-b" x="-10%" y="-10%" width="130%" height="130%">
          <feDropShadow dx="4" dy="3" stdDeviation="4" flood-color="#000" flood-opacity="0.45"/>
        </filter>
      </defs>
      <path d="M0,0 H358 C378,140 270,270 0,287 V0 Z" fill="var(--envelope-dark)" filter="url(#curve-shadow-b)"/>
    </svg>
    <div class="return-address">
      <div class="return-address__note">If undelivered please return to:</div>
      <div class="return-address__name"><span class="primary">Pixel Harbour</span> <span class="accent">Co</span></div>
      <div>17b Tamsin Crescent</div>
      <div>Larkfield, Vic, 3198</div>
    </div>
    <div class="address-window"></div>
    <div class="brand-mark">
      <div class="brand-mark__dot"></div>
      <div class="brand-mark__name">PIXEL HARBOUR CO</div>
    </div>
  </section>
  <div class="caption caption--window">DL Window Envelope</div>

</main>
</body>
</html>
```